Business / Stationery Design Project

Hi,

I need business cards and all other stationary designed for my new finance broking business.

Stationary required:

Business card
Letter head
with compliments
envelopes

There is gold in the logo design so some gold would be good and open to other creative ideas / colours.

Regards
Milo
Updates

Target Market(s)

Small to medium business customers. Also to appeal to referrers who include accounting firms and other associated professionals (valuers etc)

Industry/Entity Type

Finance

Requirements
Must have
• Professional, classy look.

```html
<!DOCTYPE html>
<html lang="en">
<head>
<meta charset="utf-8">
<title>Harlow Finance – Business Cards</title>
<link rel="stylesheet" href="https://fonts.googleapis.com/css2?family=Source+Sans+3:wght@400;600;700&display=swap">
<style>
  :root {
    --page-bg: #efede9;
    --card-white: #ffffff;
    --ink: #111111;
    --ink-soft: #4a4a4a;
    --icon: #555555;
    --gold: #c9a263;
    --gold-light: #e2c896;
    --gold-deep: #b88f4f;
    --band-black: #0c0c0c;
  }
  * { box-sizing: border-box; margin: 0; padding: 0; }
  html, body {
    width: 1074px;
    height: 1200px;
    overflow: hidden;
  }
  body {
    background: var(--page-bg);
    font-family: "Source Sans 3", Arial, sans-serif;
    position: relative;
  }
  .card {
    position: absolute;
    left: 187px;
    width: 700px;
    height: 430px;
    border-radius: 36px;
    overflow: hidden;
    background: var(--card-white);
    box-shadow: 0 10px 28px rgba(0,0,0,0.18);
  }
  .card--front { top: 110px; }
  .card--back { top: 650px; }
  .card__bands {
    position: absolute;
    inset: 0;
    width: 100%;
    height: 100%;
  }
  .brand-name {
    position: absolute;
    color: var(--ink);
    font-weight: 600;
    text-transform: uppercase;
    letter-spacing: 2px;
    line-height: 1;
    white-space: nowrap;
  }
  .brand-name__sub {
    display: block;
    font-size: 0.34em;
    letter-spacing: 0.6em;
    margin-top: 10px;
    padding-left: 0.6em;
  }
  .card--front .brand-name { left: 60px; top: 130px; font-size: 60px; }
  .card--back .brand-name { left: 150px; top: 170px; font-size: 66px; }

  .holder {
    position: absolute;
    right: 44px;
    top: 40px;
    text-align: right;
    color: var(--card-white);
  }
  .holder__name { font-size: 24px; font-weight: 700; color: var(--card-white); }
  .holder__title { font-size: 15px; font-weight: 400; color: var(--card-white); }

  .address {
    position: absolute;
    right: 50px;
    top: 302px;
    text-align: right;
    color: var(--ink);
    font-size: 18px;
    line-height: 1.3;
  }
  .contacts {
    position: absolute;
    left: 40px;
    top: 292px;
    list-style: none;
    color: var(--ink-soft);
    font-size: 15px;
    line-height: 20px;
    white-space: nowrap;
  }
  .contacts li { display: flex; align-items: center; gap: 6px; }
  .contacts svg { width: 13px; height: 13px; flex: none; }
  .web-address {
    position: absolute;
    right: 64px;
    bottom: 38px;
    color: var(--ink);
    font-size: 22px;
    font-weight: 700;
  }
</style>
</head>
<body>

<svg width="0" height="0" style="position:absolute">
  <defs>
    <linearGradient id="gold-sheen" x1="0" y1="0" x2="1" y2="1">
      <stop offset="0" style="stop-color: var(--gold-light)"/>
      <stop offset="0.5" style="stop-color: var(--gold)"/>
      <stop offset="1" style="stop-color: var(--gold-deep)"/>
    </linearGradient>
  </defs>
</svg>

<section class="card card--front" aria-label="Business card front">
  <svg class="card__bands" viewBox="0 0 700 430" preserveAspectRatio="none" aria-hidden="true">
    <rect width="700" height="430" fill="url(#gold-sheen)"/>
    <path d="M470,0 H700 V95 C560,175 420,330 250,430 H180 C360,330 470,210 470,0 Z" style="fill: var(--band-black)"/>
    <path d="M0,0 H470 C470,210 360,330 180,430 H0 Z" style="fill: var(--card-white)"/>
  </svg>

  <div class="brand-name">Harlow<span class="brand-name__sub">Finance</span></div>

  <div class="holder">
    <div class="holder__name">Greg Milo</div>
    <div class="holder__title">Title</div>
  </div>

  <div class="address">111, Street #, Suit #,<br>City Name, State 111 222</div>

  <ul class="contacts">
    <li><svg viewBox="0 0 14 14"><circle cx="7" cy="7" r="7" style="fill: var(--icon)"/><path d="M4.5,3.5 l1.5,1.5 -0.8,1 a5,5 0 0 0 2.8,2.8 l1-0.8 1.5,1.5 -1,1 a6,6 0 0 1 -6-6 z" fill="#fff"/></svg>(111)222-333</li>
    <li><svg viewBox="0 0 14 14"><circle cx="7" cy="7" r="7" style="fill: var(--icon)"/><rect x="5" y="3" width="4" height="8" rx="1" fill="#fff"/></svg>(111)222-333</li>
    <li><svg viewBox="0 0 14 14"><circle cx="7" cy="7" r="7" style="fill: var(--icon)"/><rect x="4" y="5" width="6" height="4" fill="#fff"/><rect x="5" y="3.5" width="4" height="1.5" fill="#fff"/></svg>(111)222-333</li>
    <li><svg viewBox="0 0 14 14"><circle cx="7" cy="7" r="7" style="fill: var(--icon)"/><circle cx="7" cy="7" r="2.5" fill="none" stroke="#fff" stroke-width="1.3"/></svg>hello@harlowfinance.com</li>
    <li><svg viewBox="0 0 14 14"><circle cx="7" cy="7" r="7" style="fill: var(--icon)"/><circle cx="7" cy="7" r="3.5" fill="none" stroke="#fff" stroke-width="1"/><line x1="3.5" y1="7" x2="10.5" y2="7" stroke="#fff" stroke-width="1"/></svg>www.website.com</li>
  </ul>
</section>

<section class="card card--back" aria-label="Business card back">
  <svg class="card__bands" viewBox="0 0 700 430" preserveAspectRatio="none" aria-hidden="true">
    <rect width="700" height="430" fill="url(#gold-sheen)"/>
    <path d="M490,0 H700 V105 C570,185 430,330 260,430 H190 C370,330 490,210 490,0 Z" style="fill: var(--band-black)"/>
    <path d="M0,0 H490 C490,210 370,330 190,430 H0 Z" style="fill: var(--card-white)"/>
  </svg>

  <div class="brand-name">Harlow<span class="brand-name__sub">Finance</span></div>

  <div class="web-address">www.website.com</div>
</section>

</body>
</html>
```